Create a bold and border around my logo to make it pop and sign graphic design

I would like someone to create a sign graphic design so I can use on the side of my trucks and put on yard signs. I would to remove a lot of the white and add more of the orange and blue to give it more pop when cars drive past. I would like the services to be removed and for you to leave space for a mobile number that i would add later. I don’t want my logo changed at all. I just want colour and design to be added to the background so i can use it in signage. Same colour as on the sign

```html
<!DOCTYPE html>
<html lang="en">
<head>
<meta charset="utf-8">
<title>Branchworthy – Vehicle and Yard Sign</title>
<link rel="stylesheet" href="https://fonts.googleapis.com/css2?family=Saira:wght@700&display=swap">
<style>
  :root {
    --sign-orange: #f07300;
    --sign-blue: #3439c8;
    --paper: #ffffff;
  }
  html, body {
    margin: 0;
    padding: 0;
    overflow: hidden;
    background: var(--paper);
  }
  .canvas {
    position: relative;
    width: 1200px;
    height: 1000px;
    background: var(--paper);
    overflow: hidden;
  }
  .sunburst {
    position: absolute;
    left: 18px;
    top: 229px;
    width: 1164px;
    height: 541px;
  }
  .ray-orange { fill: var(--sign-orange); }
  .ray-blue { fill: var(--sign-blue); }
  .brand-ring {
    position: absolute;
    left: 465px;
    top: 296px;
    width: 270px;
    height: 270px;
  }
  .brand-ring circle {
    fill: none;
    stroke: var(--paper);
    stroke-width: 16;
  }
  .name-plate,
  .phone-plate {
    position: absolute;
    background: var(--paper);
    display: flex;
    align-items: center;
    justify-content: center;
    font-family: "Saira", sans-serif;
    font-weight: 700;
    color: var(--sign-blue);
    text-transform: uppercase;
    line-height: 1;
  }
  .name-plate {
    left: 280px;
    top: 587px;
    width: 640px;
    height: 75px;
    border-radius: 11px;
    font-size: 58px;
    letter-spacing: 3px;
  }
  .phone-plate {
    left: 403px;
    top: 684px;
    width: 392px;
    height: 53px;
    border-radius: 9px;
    font-size: 42px;
    letter-spacing: 4px;
  }
</style>
</head>
<body>
  <main class="canvas">
    <svg class="sunburst" viewBox="18 229 1164 541" xmlns="http://www.w3.org/2000/svg" aria-hidden="true">
      <rect class="ray-blue" x="18" y="229" width="1164" height="541"/>
      <polygon class="ray-orange" points="18,229 131,229 600,500 18,500"/>
      <polygon class="ray-orange" points="444,229 600,229 600,500"/>
      <polygon class="ray-orange" points="756,229 1068,229 600,500"/>
      <polygon class="ray-orange" points="131,770 444,770 600,500"/>
      <polygon class="ray-orange" points="600,500 756,770 600,770"/>
      <polygon class="ray-orange" points="600,500 1182,500 1182,770 1068,770"/>
    </svg>

    <svg class="brand-ring" viewBox="0 0 270 270" xmlns="http://www.w3.org/2000/svg" aria-hidden="true">
      <circle cx="135" cy="135" r="126"/>
    </svg>

    <div class="name-plate">Branchworthy</div>
    <div class="phone-plate">0275550194</div>
  </main>
</body>
</html>
```